Flyer Design For Tech Support Company

We need a flyer design for our company Corvalo Tailored Device Services Ltd. I would like this to follow the same theme and styling of: www.corvalodevice.co.uk I would also invite you to use any information as found on our site. I would like this to focues primarily on attracting small bussines/start-up new custom; additionaly if there could be a mention of being able to work with private customers also.

Target Market(s)

Start-up, Small Businnes, Private Home.

Industry/Entity Type

It Company

Font styles to use
Sans Serif

Colors
33a6d7

Requirements
Must have
• Follow theme/style of main site.
• Be bold to attract from a distance.
Should not have
• Funny's

```html
<!DOCTYPE html>
<html lang="en">
<head>
<meta charset="utf-8">
<title>Corvalo Tailored Device Services – Flyer</title>
<link rel="stylesheet" href="https://fonts.googleapis.com/css2?family=Signika:wght@400;500;600&family=Encode+Sans+Condensed:wght@300;400;600&display=swap">
<style>
  :root {
    --brand: #33a6d7;
    --brand-deep: #1b7fc0;
    --sky-light: #8fd0f0;
    --sky-mid: #4fb3e6;
    --ink: #111820;
    --body: #4a4f55;
    --paper: #ffffff;
    --canvas: #ffffff;
  }
  * { margin: 0; padding: 0; box-sizing: border-box; }
  html, body { width: 1200px; height: 849px; overflow: hidden; background: var(--canvas); }
  body { position: relative; font-family: "Encode Sans Condensed", "Arial Narrow", sans-serif; color: var(--body); }

  .page { position: absolute; top: 51px; width: 525px; height: 745px; overflow: hidden; box-shadow: 0 2px 8px rgba(0,0,0,.25); }
  .page--front { left: 65px; background: var(--brand); }
  .page--back { left: 610px; background: var(--paper); }

  /* Front */
  .sky { position: absolute; left: 0; width: 100%; background: radial-gradient(ellipse at 20% 30%, var(--sky-light) 0%, transparent 45%), radial-gradient(ellipse at 80% 75%, #7cc6ec 0%, transparent 50%), linear-gradient(180deg, var(--brand-deep) 0%, var(--sky-mid) 45%, #3a9fdc 100%); }
  .sky--top { top: 0; height: 547px; }
  .sky--bottom { top: 660px; height: 85px; }

  .badge { position: absolute; left: 106px; top: 77px; width: 324px; height: 324px; border-radius: 50%; background: var(--paper); box-shadow: 4px 6px 14px rgba(0,0,0,.3); display: flex; flex-direction: column; align-items: center; justify-content: center; text-align: center; }
  .badge__name { font-family: "Signika", sans-serif; font-weight: 400; color: var(--brand); font-size: 34px; line-height: 1.15; letter-spacing: .5px; }

  .front__tagline { position: absolute; left: 0; width: 100%; top: 485px; text-align: center; font-family: "Signika", sans-serif; font-weight: 500; font-size: 28px; line-height: 32px; color: var(--paper); text-shadow: 1px 2px 4px rgba(0,0,0,.35); }

  .contact { position: absolute; left: 0; top: 547px; width: 100%; height: 113px; background: var(--paper); display: flex; flex-direction: column; align-items: center; justify-content: center; gap: 3px; font-family: "Signika", sans-serif; font-size: 19px; color: #333a40; }
  .contact__line { display: flex; align-items: center; gap: 6px; }
  .contact__icon { width: 18px; height: 18px; }

  .front__web { position: absolute; left: 0; width: 100%; top: 683px; text-align: center; font-family: "Signika", sans-serif; font-size: 22px; color: var(--paper); text-shadow: 1px 2px 3px rgba(0,0,0,.3); }

  /* Back */
  .back__sky { position: absolute; left: 0; top: 0; width: 100%; height: 260px; background: linear-gradient(180deg, #dfe8ee 0%, #f1f5f8 50%, var(--paper) 100%); }
  .back__headline { position: absolute; left: 0; top: 48px; width: 100%; text-align: center; font-family: "Signika", sans-serif; font-weight: 600; font-size: 38px; line-height: 34.5px; color: var(--brand); }
  .back__intro { position: absolute; left: 50px; width: 425px; top: 170px; text-align: center; font-weight: 600; font-size: 11.6px; line-height: 12.6px; color: var(--ink); }
  .back__lead { position: absolute; left: 45px; width: 435px; top: 229px; text-align: center; font-weight: 300; font-size: 9.7px; line-height: 12.8px; color: var(--body); }

  .feature { position: absolute; left: 58px; width: 430px; }
  .feature__icon { position: absolute; left: 0; top: 0; width: 48px; height: 48px; }
  .feature__title { margin-left: 64px; font-family: "Signika", sans-serif; font-weight: 500; font-size: 23px; line-height: 24px; color: var(--brand); }
  .feature__text { margin-left: 64px; margin-top: 2px; font-weight: 300; font-size: 9.8px; line-height: 12.7px; color: var(--body); }
  .feature--cost { top: 300px; }
  .feature--experience { top: 400px; }
  .feature--pro { top: 517px; }
  .feature--support { top: 621px; }

  .back__cta { position: absolute; left: 0; top: 694px; width: 100%; height: 51px; background: var(--brand); display: flex; align-items: center; justify-content: center; font-weight: 600; font-size: 11.5px; color: var(--paper); }
</style>
</head>
<body>

<section class="page page--front">
  <div class="sky sky--top" role="img" aria-label="Blue sky with soft white clouds"></div>
  <div class="badge">
    <p class="badge__name">Corvalo<br>Tailored Device Services</p>
  </div>
  <h1 class="front__tagline">FOR ALL YOUR SMALL BUSINESS<br>TECHNOLOGY NEEDS</h1>

  <div class="contact">
    <p class="contact__line">
      <svg class="contact__icon" viewBox="0 0 20 20"><path d="M10 1a6 6 0 0 0-6 6c0 4.5 6 12 6 12s6-7.5 6-12a6 6 0 0 0-6-6z" fill="var(--brand)"/><circle cx="10" cy="7" r="2.3" fill="#fff"/></svg>
      Brackenford, North Lanarkshire
    </p>
    <p class="contact__line">
      <svg class="contact__icon" viewBox="0 0 20 20"><path d="M5 2l3 4-2 2c1 2.5 3 4.5 5.5 5.5l2-2 4 3-2 3c-6 0-13-7-13-13z" fill="none" stroke="var(--brand)" stroke-width="1.4" stroke-linejoin="round"/></svg>
      +44 7700 900418
    </p>
    <p class="contact__line">
      <svg class="contact__icon" viewBox="0 0 20 20"><rect x="1.5" y="4" width="17" height="12" fill="none" stroke="var(--brand)" stroke-width="1.4"/><path d="M1.5 4l8.5 7 8.5-7" fill="none" stroke="var(--brand)" stroke-width="1.4"/></svg>
      info@corvalodevice.co.uk
    </p>
  </div>

  <div class="sky sky--bottom" role="img" aria-label="Blue sky with soft white clouds"></div>
  <p class="front__web">www.corvalodevice.co.uk</p>
</section>

<section class="page page--back">
  <div class="back__sky" role="img" aria-label="Pale sky with faint clouds"></div>
  <h2 class="back__headline">We are here to meet your<br>technology needs and<br>exceed your expectations</h2>
  <p class="back__intro">Welcome to Corvalo Tailored Device Services Ltd., a professional company formed to meet your demands and exceed your expectations. From the smallest to the most complex technological need; from home computer troubleshooting to a custom designed and fitted tech solution – we are here to support you.</p>
  <p class="back__lead">Passion, the backbone of our business, and the reason we exist. Formed in 2015 to meet the ever-changing demands of our clients, to infuse our passion for technology with the on-going desire for supporting our clients' needs. We will take the formation of an idea, create a concept and work with our clients in realising that idea. At Corvalo, we realise that our clients' needs are ever changing and we look forward to supporting you every step of the way.</p>

  <article class="feature feature--cost">
    <svg class="feature__icon" viewBox="0 0 48 48"><circle cx="24" cy="24" r="23" fill="var(--brand)"/><circle cx="24" cy="24" r="18" fill="#2a8fc4"/><text x="24" y="33" text-anchor="middle" font-family="Signika, sans-serif" font-weight="600" font-size="26" fill="#fff">$</text></svg>
    <h3 class="feature__title">COST EFFECTIVE</h3>
    <p class="feature__text">We understand that no matter how small your problem may be or how big a solution you need, price is an important factor. We listen to our clients' needs and expectations, we answer your queries and we build up a dedicated package for you. No added extras, no gimmicks, just a solution. We are bespoke, that's what we do!</p>
  </article>

  <article class="feature feature--experience">
    <svg class="feature__icon" viewBox="0 0 48 48"><circle cx="24" cy="26" r="21" fill="var(--brand)"/><path d="M13 26l8 8 18-20" fill="none" stroke="#fff" stroke-width="5" stroke-linecap="round" stroke-linejoin="round"/></svg>
    <h3 class="feature__title">EXPERIENCED</h3>
    <p class="feature__text">With over 10 years of technology experience and training. Take the top line training and add it to a career employing and developing these skills as a Coastal Fleet Service Engineer and you get a technician and consultant who lives and breaths technology. Technology changes and advances and so does our training, we continually train and develop our staff so we can better meet, understand and support your demands and needs.</p>
  </article>

  <article class="feature feature--pro">
    <svg class="feature__icon" viewBox="0 0 48 48"><circle cx="24" cy="24" r="23" fill="var(--brand)"/><circle cx="19" cy="19" r="5" fill="#fff"/><path d="M10 34c0-7 4-10 9-10s9 3 9 10z" fill="#fff"/><circle cx="30" cy="18" r="4.5" fill="#fff"/><path d="M26 34c1-6 2-9 4-10 5 0 8 3 8 10z" fill="#fff"/></svg>
    <h3 class="feature__title">PROFESSIONAL</h3>
    <p class="feature__text">It's your home, it's your office – when you invite us to work with you on your bespoke solution, you will receive a professional experience; from the first phone call through to the on-going support you will receive. When you meet our staff, you will be met with the utmost professionalism. We realise that you may have taken time off for our visit and as such will always endeavour to be there at the agreed time.</p>
  </article>

  <article class="feature feature--support">
    <svg class="feature__icon" viewBox="0 0 48 48"><circle cx="24" cy="24" r="23" fill="var(--brand)"/><path d="M13 22a11 11 0 0 1 19-6" fill="none" stroke="#fff" stroke-width="4"/><path d="M29 10l6 7-8 2z" fill="#fff"/><path d="M35 26a11 11 0 0 1-19 6" fill="none" stroke="#fff" stroke-width="4"/><path d="M19 38l-6-7 8-2z" fill="#fff"/></svg>
    <h3 class="feature__title">SUPPORT</h3>
    <p class="feature__text">Our support service is where the magic happens and exists in two main formats: our Installation Support Service and our unique "Ever-Ready" Support Service.</p>
  </article>

  <p class="back__cta">Please give us a ring or drop us an e-mail so that we can discuss what we can do for you.</p>
</section>

</body>
</html>
```